Restaurant needs a vertical banner for fried catfish

Our restaurant is looking for an eye-catching 78.75in. x 36in. vertical physical banner ad for our fried catfish. Photos for the fried catfish will be provided as a reference but we will also accept anything similar to the photo. We will be using the following as our receptacle: https://www.plankoria.example/banner-stand/retractable-banner-stands/
The design must incorporate the following flavor texts:
Fried Catfish
Always Fresh!
Made from Scratch
Hand-cut Fillets
The Best Catfish in Texas
Served with fries, hush puppies, and a 32oz fountain drink
Also available by the pound!
The final design should be creative, professional, and eye-catching for customers.
Updates
Colors
Designer to choose colors to be used in the design.
Requirements
Must have
- We are open to any and all design elements, albeit the 'flavor texts' should not overpower, but complement the fried catfish photo. 'Fried Catfish' can be used in lieu of a main title/logo.
Nice to have
- Transparent or textured backgrounds that can encompass any or all part of the banner such as a cutting board, shadows, abstract, etc to show depth are a plus.
- Use of vectors or objects such as ribbons or shapes to encapsulate the 'flavor texts' are also encouraged.

```html
<!DOCTYPE html>
<html lang="en">
<head>
<meta charset="UTF-8">
<title>Fried Catfish Vertical Banner</title>
<link href="https://fonts.googleapis.com/css2?family=Bangers&family=Bebas+Neue&family=Courier+Prime:wght@700&display=swap" rel="stylesheet">
<style>
  :root {
    --stage-top: #bdbdbd;
    --stage-bottom: #f2f2f2;
    --wall: #ebebeb;
    --wall-line: #dcdcdc;
    --orange-hot: #ff5a00;
    --orange-warm: #ffb000;
    --ink: #141414;
    --white: #ffffff;
    --ribbon-red: #e40f0f;
    --ribbon-yellow: #ffc400;
    --photo-deep: #9a5412;
    --photo-gold: #d89a35;
    --photo-light: #efd9a0;
  }
  * { box-sizing: border-box; margin: 0; padding: 0; }
  html, body { width: 1200px; height: 1200px; overflow: hidden; }
  body {
    background: linear-gradient(180deg, var(--stage-top), var(--stage-bottom));
    position: relative;
  }
  .banner {
    position: absolute;
    left: 344px; top: 40px;
    width: 512px; height: 1120px;
    overflow: hidden;
    background:
      repeating-linear-gradient(0deg, var(--wall) 0 30px, var(--wall-line) 30px 32px),
      var(--wall);
    box-shadow: 0 10px 30px rgba(0,0,0,.25);
  }
  .title {
    position: absolute;
    left: 0; right: 0; top: 52px;
    text-align: center;
    font-family: "Bangers", cursive;
    line-height: .9;
    color: var(--orange-hot);
    text-shadow:
      -3px -3px 0 var(--white), 3px -3px 0 var(--white),
      -3px 3px 0 var(--white), 3px 3px 0 var(--white),
      7px 7px 0 var(--ink);
  }
  .title__line { display: block; }
  .title__line--fried { font-size: 118px; padding-left: 20px; color: #ff7000; }
  .title__line--catfish { font-size: 132px; letter-spacing: 1px; color: #ff8a00; }
  .photo {
    position: absolute;
    left: 0; right: 0; top: 297px; height: 465px;
    background:
      radial-gradient(ellipse at 35% 55%, var(--photo-gold) 0%, var(--photo-deep) 55%, transparent 75%),
      linear-gradient(170deg, #b8482e 0%, var(--photo-light) 20%, var(--photo-gold) 55%, #e6b55a 100%);
  }
  .ribbon {
    position: absolute;
    left: 50%;
    display: flex; align-items: center; justify-content: center;
  }
  .ribbon svg { position: absolute; inset: 0; width: 100%; height: 100%; }
  .ribbon__text {
    position: relative;
    font-family: "Bebas Neue", sans-serif;
    white-space: nowrap;
  }
  .ribbon--fresh {
    top: 274px; width: 330px; height: 56px;
    transform: translateX(-50%) rotate(-1deg);
  }
  .ribbon--fresh .ribbon__text { font-size: 40px; letter-spacing: 2px; color: var(--ink); }
  .ribbon--red .ribbon__text { color: var(--white); font-size: 38px; letter-spacing: .5px; }
  .ribbon--scratch { top: 708px; width: 356px; height: 62px; transform: translateX(-50%) rotate(-3deg); }
  .ribbon--fillets { top: 774px; width: 316px; height: 62px; transform: translateX(-50%) rotate(-3deg); }
  .ribbon--texas { top: 842px; width: 384px; height: 66px; transform: translateX(-50%) rotate(-3deg); }
  .served {
    position: absolute;
    left: 0; right: 0; top: 936px;
    text-align: center;
    font-family: "Courier Prime", monospace;
    font-weight: 700;
    font-size: 20px;
    line-height: 1.2;
    color: var(--ink);
    transform: rotate(-5deg);
  }
  .pound {
    position: absolute;
    left: 58px; top: 1000px;
    width: 360px; height: 48px;
    background: var(--ribbon-yellow);
    display: flex; align-items: center; justify-content: center;
    font-family: "Courier Prime", monospace;
    font-weight: 700;
    font-size: 19px;
    color: var(--ink);
    transform: rotate(-4deg);
  }
</style>
</head>
<body>
  <main class="banner">
    <div class="photo" role="img" aria-label="Photo of golden fried catfish fillets with fries, hush puppies, tartar sauce and fresh vegetables"></div>

    <h1 class="title">
      <span class="title__line title__line--fried">FRIED</span>
      <span class="title__line title__line--catfish">CATFISH</span>
    </h1>

    <div class="ribbon ribbon--fresh">
      <svg viewBox="0 0 330 56" preserveAspectRatio="none" aria-hidden="true"><polygon points="0,0 330,0 312,28 330,56 0,56 18,28" fill="var(--ribbon-yellow)"/></svg>
      <span class="ribbon__text">ALWAYS FRESH!</span>
    </div>

    <div class="ribbon ribbon--red ribbon--scratch">
      <svg viewBox="0 0 356 62" preserveAspectRatio="none" aria-hidden="true"><polygon points="0,0 356,0 336,31 356,62 0,62 20,31" fill="var(--ribbon-red)"/></svg>
      <span class="ribbon__text">MADE FROM SCRATCH</span>
    </div>

    <div class="ribbon ribbon--red ribbon--fillets">
      <svg viewBox="0 0 316 62" preserveAspectRatio="none" aria-hidden="true"><polygon points="0,0 316,0 296,31 316,62 0,62 20,31" fill="var(--ribbon-red)"/></svg>
      <span class="ribbon__text">HAND-CUT FILLETS</span>
    </div>

    <div class="ribbon ribbon--red ribbon--texas">
      <svg viewBox="0 0 384 66" preserveAspectRatio="none" aria-hidden="true"><polygon points="0,0 384,0 362,33 384,66 0,66 22,33" fill="var(--ribbon-red)"/></svg>
      <span class="ribbon__text">THE BEST CATFISH IN TEXAS</span>
    </div>

    <p class="served">Served with fries, hush puppies,<br>and a 32oz fountain drink</p>

    <p class="pound">Also available by the pound!</p>
  </main>
</body>
</html>
```